New Business Card Design Project

Hi there

Could you please make a design that is soft and appealing to people who would purchase gemstones, buy healing jewellery, seek counselling, may seek energy healing and/or learn English. Essentially I'm looking for something with a soft human design. Please incorporate the logo and select font that can be easily read and softer images in the background - but not too busy. I would like it double sided as well.

Optional: Elements could include gemstones, feathers, plants and images that are happy and calming.

Target Market(s)

People into alternative health, those from non-English speaking backgrounds, businesses

Contact Information for Business Card

Tess Warbury
Mobile: 0412 385 907, Facebook and Instagram Logos,
ABN: 61 742 118 053 (Australian Business Number - small at the bottom)

Requirements
Must have
• My project must have:
- Meadow Hearth logo
- Symbols that represent the 4 main services: 1. Gemstones/jewellery, 2. counselling, 3. meditation/energy healing, 4. education
Nice to have
• Clear and easy to read.

```html
<!DOCTYPE html>
<html lang="en">
<head>
<meta charset="utf-8">
<title>Meadow Hearth – Business Card</title>
<link href="https://fonts.googleapis.com/css2?family=Lato:wght@400;700;900&display=swap" rel="stylesheet">
<style>
  :root {
    --stage: #cfd0cb;
    --card: #ffffff;
    --teal: #16ada0;
    --green: #7bb534;
    --lime: #8cc63f;
    --ink-white: #ffffff;
    --shadow: rgba(60, 60, 55, 0.28);
  }
  html, body {
    margin: 0;
    padding: 0;
    width: 1200px;
    height: 801px;
    overflow: hidden;
    background: var(--stage);
    font-family: "Lato", Arial, sans-serif;
  }
  .stage {
    position: relative;
    width: 1200px;
    height: 801px;
  }
  .card {
    position: absolute;
    top: 245px;
    width: 540px;
    height: 310px;
    background: var(--card);
    box-shadow: 0 8px 22px var(--shadow);
    overflow: hidden;
  }
  .card--front { left: 45px; }
  .card--back { left: 615px; }

  .brand {
    position: absolute;
    display: flex;
    flex-direction: column;
    align-items: center;
  }
  .brand__mark {
    width: 58px;
    height: 58px;
    border: 3px solid var(--teal);
    border-radius: 50%;
    box-sizing: border-box;
    margin-bottom: 10px;
  }
  .brand__name {
    font-weight: 400;
    font-size: 27px;
    letter-spacing: 1px;
    color: var(--green);
    white-space: nowrap;
  }
  .card--front .brand { left: 30px; top: 100px; width: 220px; }

  .divider {
    position: absolute;
    left: 268px;
    top: 70px;
    width: 1.5px;
    height: 130px;
    background: var(--teal);
  }

  .contact {
    position: absolute;
    left: 298px;
    top: 66px;
  }
  .contact__name {
    margin: 0 0 12px;
    font-weight: 900;
    font-size: 27px;
    color: var(--teal);
  }
  .contact__list {
    list-style: none;
    margin: 0;
    padding: 0;
  }
  .contact__item {
    display: flex;
    align-items: center;
    gap: 9px;
    font-size: 14.5px;
    line-height: 24px;
    color: var(--green);
    white-space: nowrap;
  }
  .contact__icon {
    width: 14px;
    height: 14px;
    flex: none;
  }

  .abn-tab {
    position: absolute;
    left: 0;
    top: 0;
    width: 540px;
    height: 310px;
  }
  .abn-tab__text {
    position: absolute;
    bottom: 10px;
    font-size: 16px;
    letter-spacing: 0.5px;
    color: var(--ink-white);
    white-space: nowrap;
  }
  .card--front .abn-tab__text { left: 358px; }
  .card--back .abn-tab__text { left: 300px; }

  .backdrop {
    position: absolute;
    inset: 0;
    background:
      radial-gradient(ellipse at 85% 30%, rgba(150, 120, 95, 0.25), transparent 55%),
      radial-gradient(ellipse at 60% 25%, rgba(120, 150, 110, 0.22), transparent 45%),
      radial-gradient(ellipse at 10% 80%, rgba(130, 120, 110, 0.22), transparent 50%),
      linear-gradient(180deg, #f5f4f0, #eeece6);
  }
  .card--back .brand { left: 170px; top: 22px; width: 200px; }

  .services {
    position: absolute;
    left: 50px;
    top: 150px;
    width: 440px;
    display: flex;
    justify-content: space-between;
  }
  .service {
    width: 78px;
    height: 78px;
    border-radius: 50%;
  }
  .service--gemstones { background: #d2442b; }
  .service--counselling { background: #e33c96; }
  .service--healing { background: radial-gradient(circle, #f5c02a 30%, #e4732a 75%); }
  .service--education { background: #222222; border-radius: 8px; }
</style>
</head>
<body>
<main class="stage">

  <section class="card card--front" aria-label="Business card, front">
    <div class="brand">
      <div class="brand__mark"></div>
      <div class="brand__name">Meadow Hearth</div>
    </div>

    <div class="divider"></div>

    <div class="contact">
      <h1 class="contact__name">Tess Warbury</h1>
      <ul class="contact__list">
        <li class="contact__item">
          <svg class="contact__icon" viewBox="0 0 14 14" aria-hidden="true">
            <path d="M3 1.5 L5.2 1.5 L6 4.2 L4.6 5.4 Q5.8 8 8.6 9.4 L9.8 8 L12.5 8.8 L12.5 11 Q12.5 12.5 11 12.5 Q1.5 12 1.5 3 Q1.5 1.5 3 1.5 Z" fill="var(--teal)"/>
          </svg>
          <span>0412 385 907</span>
        </li>
        <li class="contact__item">
          <svg class="contact__icon" viewBox="0 0 14 14" aria-hidden="true">
            <circle cx="7" cy="7" r="6" fill="none" stroke="var(--teal)" stroke-width="1.5"/>
          </svg>
          <span>meadowhearth.com.au/connect</span>
        </li>
        <li class="contact__item">
          <svg class="contact__icon" viewBox="0 0 14 14" aria-hidden="true">
            <circle cx="7" cy="7" r="6" fill="none" stroke="var(--teal)" stroke-width="1.5"/>
          </svg>
          <span>@MeadowHearth</span>
        </li>
      </ul>
    </div>

    <svg class="abn-tab" viewBox="0 0 540 310" aria-hidden="true">
      <path d="M330 310 V292 Q330 272 352 272 H540 V310 Z" fill="var(--teal)"/>
      <path d="M326 310 V292 Q326 268 352 268 H540" fill="none" stroke="var(--lime)" stroke-width="3"/>
    </svg>
    <div class="abn-tab__text">ABN: 61 742 118 053</div>
  </section>

  <section class="card card--back" aria-label="Business card, back">
    <div class="backdrop" role="img" aria-label="Soft, faded photo of crystals, gemstones, leaves and a feather"></div>

    <div class="brand">
      <div class="brand__mark"></div>
      <div class="brand__name">Meadow Hearth</div>
    </div>

    <div class="services">
      <div class="service service--gemstones" role="img" aria-label="Red faceted gemstone illustration"></div>
      <div class="service service--counselling" role="img" aria-label="Pink head with brain illustration"></div>
      <div class="service service--healing" role="img" aria-label="Meditating figure before a sun illustration"></div>
      <div class="service service--education" role="img" aria-label="Open book illustration"></div>
    </div>

    <svg class="abn-tab" viewBox="0 0 540 310" aria-hidden="true">
      <path d="M270 310 V292 Q270 272 292 272 H540 V310 Z" fill="var(--teal)"/>
      <path d="M266 310 V292 Q266 268 292 268 H540" fill="none" stroke="var(--lime)" stroke-width="3"/>
    </svg>
    <div class="abn-tab__text">ABN: 61 742 118 053</div>
  </section>

</main>
</body>
</html>
```